M Zyvantics Buisness Cards

I need a technology focused clean business card for my employees. I have attached out logo to include in the mocks. We're a modern tech consulting firm that drives to interface humanity with technology in a truly cohesive fashion.

```html
<!DOCTYPE html>
<html lang="en">
<head>
<meta charset="utf-8">
<title>M Zyvantics Business Cards</title>
<link href="https://fonts.googleapis.com/css2?family=Work+Sans:wght@400;500;600&display=swap" rel="stylesheet">
<style>
  :root {
    --brand-blue: #0b75c4;
    --card-white: #ffffff;
    --accent-grey: #8a8d91;
    --backdrop: #2b2b2d;
  }
  * { margin: 0; padding: 0; box-sizing: border-box; }
  html, body { width: 1200px; height: 930px; overflow: hidden; }
  body {
    background: var(--backdrop);
    font-family: "Work Sans", sans-serif;
    position: relative;
  }
  .card {
    position: absolute;
    left: 290px;
    width: 620px;
    height: 354px;
    border-radius: 18px;
    background: var(--brand-blue);
    overflow: hidden;
    color: var(--card-white);
  }
  .card-back { top: 64px; display: flex; align-items: center; justify-content: center; }
  .card-front { top: 508px; }
  .wordmark {
    display: flex; align-items: center; gap: 14px;
    font-weight: 600; letter-spacing: 1px; color: var(--card-white);
  }
  .wordmark-dot { border-radius: 50%; background: var(--card-white); flex: none; }
  .card-back .wordmark { font-size: 52px; }
  .card-back .wordmark-dot { width: 38px; height: 38px; }
  .front-shape { position: absolute; inset: 0; }
  .front-info { position: absolute; left: 34px; top: 40px; }
  .card-front .wordmark { font-size: 30px; gap: 10px; }
  .card-front .wordmark-dot { width: 24px; height: 24px; }
  .person-name { margin-top: 34px; font-size: 23px; font-weight: 600; text-transform: uppercase; letter-spacing: .3px; }
  .person-role { font-size: 15px; margin-top: 2px; }
  .address { margin-top: 16px; font-size: 14px; line-height: 1.35; }
  .contacts { margin-top: 14px; list-style: none; font-size: 14px; line-height: 1.45; }
  .contacts li { display: flex; align-items: center; gap: 8px; }
  .contacts svg { width: 11px; height: 11px; flex: none; }
  .circle-name {
    position: absolute; left: 380px; top: 132px; width: 200px; text-align: center;
    font-size: 30px; font-weight: 600; color: var(--brand-blue);
  }
</style>
</head>
<body>
  <section class="card card-back">
    <div class="wordmark"><span class="wordmark-dot"></span>M Zyvantics</div>
  </section>

  <section class="card card-front">
    <svg class="front-shape" viewBox="0 0 620 354" aria-hidden="true">
      <circle cx="468" cy="160" r="190" fill="var(--accent-grey)" opacity=".55"/>
      <rect x="478" y="0" width="142" height="250" fill="var(--card-white)"/>
      <circle cx="478" cy="156" r="190" fill="var(--card-white)"/>
    </svg>
    <div class="circle-name">M Zyvantics</div>
    <div class="front-info">
      <div class="wordmark"><span class="wordmark-dot"></span>M Zyvantics</div>
      <div class="person-name">Dorian Vale</div>
      <div class="person-role">Director</div>
      <div class="address">820 Larkspur Field Rd<br>Alder Bay, CA 90210-4418</div>
      <ul class="contacts">
        <li><svg viewBox="0 0 12 12"><path d="M3 1l2 2-1 1.5a7 7 0 0 0 3.5 3.5L9 7l2 2-1.5 2A9 9 0 0 1 1 2.5z" fill="currentColor"/></svg>555-014-2297</li>
        <li><svg viewBox="0 0 12 12"><rect x="1" y="2.5" width="10" height="7" fill="none" stroke="currentColor"/><path d="M1 2.5l5 4 5-4" fill="none" stroke="currentColor"/></svg>info@mzyvantics.com</li>
        <li><svg viewBox="0 0 12 12"><circle cx="6" cy="6" r="5" fill="none" stroke="currentColor"/><path d="M1 6h10M6 1c-3 3-3 7 0 10M6 1c3 3 3 7 0 10" fill="none" stroke="currentColor"/></svg>www.mzyvantics.com</li>
      </ul>
    </div>
  </section>
</body>
</html>
```